New Business and Accounting Software need a Web Site

The website is for a Business and Accounting Software that has 8 products.
Each product has its owns logo and color, when you do the design have in consideration that we are looking the experience that when you change from one product page to another the look and feel adjust to the color and logo of the product.
The product are:
Ventas (Sales)
Compras (Purchases)
Contabilidad (Accounting)
Presupuesto (Budget)
Inventarios (Inventory)
Bancos (Banks)
NĂ³mina RH (Human Resources Payroll)
CRM (Customer Relationship Manager)

You can see how the main logo and variations are used in each page
- https://www.ufta.com/
- https://www.vemi.com/
- https://www.prulvin.com/

Our goal is to be similar to them.

I have created a word document to explain what I want.
You need to design:
1 Home Page
1 Product Landing Page
1 Product Detail Page
1 Price Page

I am attaching:
1. Main Logo
2. 8 Product Logos
3. Website Idea, you can create your own idea.

You are welcome to use other icons for the each product if you want.

Target Market(s)

Independet professionals and Small and Medium Companies

Industry/Entity Type

Business and Accounting Software

Coding

Coded - Design and coding required

Colors
0054AA
0677BA
7BADD7
CADEEF
E8F1F8

Requirements
Must have
• Must show all products in the main page

```html
<!DOCTYPE html>
<html lang="es">
<head>
<meta charset="utf-8">
<title>Cuentix — Software de negocios y contabilidad</title>
<link href="https://fonts.googleapis.com/css2?family=Questrial&family=Lato:wght@400;700&display=swap" rel="stylesheet">
<style>
:root{
  --blue:#0054AA;
  --blue-mid:#0677BA;
  --blue-light:#7BADD7;
  --blue-pale:#CADEEF;
  --blue-ice:#E8F1F8;
  --red:#D4401F;
  --black:#050505;
  --ink:#222;
  --muted:#555;
  --grey-bg:#F4F4F4;
  --white:#fff;
}
*{box-sizing:border-box;margin:0;padding:0}
html,body{width:1200px;height:4158px;overflow:hidden}
body{position:relative;background:var(--white);font-family:'Lato',sans-serif;color:var(--ink)}
.abs{position:absolute}
.head-font{font-family:'Questrial',sans-serif}
a{color:inherit;text-decoration:none}

/* header */
.site-header{left:0;top:0;width:1200px;height:104px}
.brand{display:flex;align-items:center;gap:10px;font-family:'Questrial',sans-serif;font-size:44px;color:var(--blue)}
.brand-dot{width:46px;height:46px;border-radius:50%;background:var(--blue)}
.site-header .brand{position:absolute;left:76px;top:26px}
.nav{position:absolute;left:442px;top:44px;display:flex;gap:38px;font-size:13px}
.nav a.active{color:var(--blue);border-bottom:2px solid var(--blue);padding-bottom:4px}
.btn{display:inline-flex;align-items:center;justify-content:center;border-radius:22px;font-size:13px;color:#fff}
.btn-quote{position:absolute;left:848px;top:31px;width:134px;height:40px;background:var(--blue)}
.btn-trial{position:absolute;left:992px;top:31px;width:134px;height:40px;background:var(--blue-light)}

/* hero */
.hero{left:0;top:104px;width:1200px;height:682px;background:var(--black);overflow:hidden}
.hero-photo{position:absolute;left:330px;top:0;width:870px;height:682px;background:linear-gradient(100deg,#2a2a2a 0%,#cfcfcf 25%,#ececec 60%,#dadada 100%)}
.hero-title{position:absolute;left:76px;top:258px;font-family:'Questrial',sans-serif;font-size:31px;line-height:37px;color:#fff}
.hero-btn{position:absolute;left:76px;top:374px;width:134px;height:40px;background:var(--blue)}
.hero-pager{position:absolute;left:80px;top:580px;display:flex;align-items:center;gap:12px;color:var(--blue-light);font-size:11px}
.hero-pager span.lines{display:flex;flex-direction:column;gap:7px}
.hero-pager span.lines i{display:block;width:30px;height:2px;background:#fff}
.hero-wave{position:absolute;left:0;top:660px}

/* products */
.section-title{width:1200px;text-align:center;font-family:'Questrial',sans-serif;color:var(--ink)}
.products-title{top:868px;font-size:34px}
.product-name{display:flex;align-items:center;justify-content:center;gap:8px;width:260px;font-family:'Questrial',sans-serif;font-size:27px;color:var(--blue);letter-spacing:1px}
.product-name i{width:30px;height:30px;border-radius:50%;background:var(--blue);display:block}
.tile{width:97px;height:96px;border-radius:16px;background:#fff;box-shadow:0 3px 8px rgba(0,0,0,.25);display:flex;flex-direction:column;align-items:center;justify-content:center;gap:6px;font-family:'Questrial',sans-serif;color:var(--blue);font-size:13px;font-weight:700}
.tile.small{font-size:9px}
.tile i{display:block;width:22px;height:22px;border-radius:50%;background:var(--blue)}
.tile i.alt{border-radius:4px;background:var(--blue-light)}
.profile-q{top:1428px;font-size:30px}

/* profile band */
.profile{top:1525px;height:491px;width:300px}
.profile.blue{background:var(--blue);color:#fff}
.profile.light{background:var(--blue-light);color:#fff}
.profile .ph{position:absolute;inset:0}
.profile h3{position:absolute;left:52px;top:72px;font-family:'Questrial',sans-serif;font-weight:400;font-size:30px}
.profile hr{position:absolute;left:52px;top:130px;width:34px;border:0;border-top:2px solid #fff}
.profile p{position:absolute;left:52px;width:220px;font-size:11.5px;line-height:21.5px}
.profile .btn{position:absolute;left:50px;height:40px;width:154px;font-size:12px}

/* plans */
.plan{top:2091px;width:251px;height:306px;color:#fff}
.plan h3{position:absolute;left:26px;top:38px;font-family:'Questrial',sans-serif;font-weight:400;font-size:30px}
.plan p{position:absolute;left:26px;top:100px;width:200px;font-size:12px;line-height:22px}
.plan a{position:absolute;left:26px;top:260px;font-size:12px;text-decoration:underline}

/* tabs */
.tab{top:2487px;width:190px;height:58px;display:flex;align-items:center;justify-content:center;font-family:'Questrial',sans-serif;font-size:19px}
.tab1{background:#F2F2F2;color:var(--ink);border-radius:8px 8px 0 0}
.tab2{background:var(--blue-light);color:#fff;border-radius:8px 8px 0 0}
.tab3{background:var(--blue);color:#fff;top:2494px;height:51px}
.tab4{background:var(--red);color:#fff;top:2494px;height:51px}
.tab-panel{left:0;top:2545px;width:1200px;height:564px;background:var(--grey-bg)}
.tab-panel h2{position:absolute;left:78px;top:60px;font-family:'Questrial',sans-serif;font-weight:400;font-size:33px}
.checklist{position:absolute;left:76px;top:115px;width:470px;list-style:none}
.checklist li{display:flex;gap:14px;font-size:12.5px;line-height:22px;color:var(--muted);margin-bottom:16px}
.checklist svg{flex:none;margin-top:2px}
.tab-panel .btn{position:absolute;left:76px;top:431px;width:154px;height:40px;background:var(--blue);font-size:12px}
.tab-photo{position:absolute;left:609px;top:58px;width:483px;height:437px;border-radius:70px 0 70px 0;background:linear-gradient(135deg,#cfd6dc,#f5f5f5 45%,#e4b540 100%)}

/* features */
.feature{top:3201px;width:251px;height:266px;color:#fff;padding:24px 34px}
.feature .num{font-family:'Questrial',sans-serif;font-size:88px;line-height:80px;font-weight:700}
.feature h4{position:absolute;left:34px;top:118px;font-family:'Questrial',sans-serif;font-weight:400;font-size:23px}
.feature p{position:absolute;left:34px;top:158px;width:190px;font-size:12px;line-height:22px}

/* cta */
.cta{left:0;top:3571px;width:1200px;height:486px;background:var(--blue)}
.cta h2{position:absolute;left:114px;top:172px;width:480px;font-family:'Questrial',sans-serif;font-weight:400;font-size:36px;line-height:41px;color:#fff}
.cta .btn{position:absolute;left:110px;top:312px;width:170px;height:38px;background:var(--blue-light);font-size:12px}
.cta-photo{left:599px;top:3511px;width:491px;height:491px;border-radius:120px 0 120px 120px;background:linear-gradient(150deg,#f3f3f3,#c9d3dc 55%,#8fa2b5)}

/* footer */
.site-footer{left:0;top:4057px;width:1200px;height:101px}
.site-footer .brand{position:absolute;left:76px;top:26px}
.newsletter-input{position:absolute;left:384px;top:28px;width:506px;height:44px;background:#F2F2F2;font-size:12px;color:var(--muted);padding:15px 20px}
.newsletter-btn{position:absolute;left:912px;top:28px;width:214px;height:44px;background:var(--blue);color:#fff;display:flex;align-items:center;justify-content:center;font-size:13px}
</style>
</head>
<body>

<header class="abs site-header">
  <div class="brand"><span class="brand-dot"></span>Cuentix</div>
  <nav class="nav">
    <a class="active" href="#">Inico</a><a href="#">Soluciones</a><a href="#">Planes</a><a href="#">Contacto</a>
  </nav>
  <a class="btn btn-quote" href="#">Get A Quote</a>
  <a class="btn btn-trial" href="#">Free Trial</a>
</header>

<section class="abs hero">
  <div class="hero-photo" role="img" aria-label="Mujer trabajando en un escritorio con monitores de hojas de cálculo"></div>
  <h1 class="hero-title" style="font-weight:400">Take More Control<br>of Your Business</h1>
  <a class="btn hero-btn" href="#">Free Trial</a>
  <div class="hero-pager">02 <span class="lines"><i></i><i></i><i></i></span></div>
</section>
<svg class="abs" style="left:0;top:690px" width="1200" height="110" viewBox="0 0 1200 110">
  <polygon points="0,96 1200,10 1200,110 0,110" fill="#fff"/>
  <path d="M432 70 L1000 40" stroke="#0054AA" stroke-width="16" stroke-linecap="round"/>
  <path d="M808 60 L1200 30" stroke="#7BADD7" stroke-width="16" stroke-linecap="round"/>
</svg>

<h2 class="abs section-title products-title" style="font-weight:400">Adquiere solo el PLAN que necesitas</h2>

<div class="abs product-name" style="left:52px;top:975px"><i></i>VENTAS</div>
<div class="abs product-name" style="left:330px;top:972px"><i></i>COMPRAS</div>
<div class="abs product-name" style="left:613px;top:970px;font-size:22px"><i></i>CONTABILIDAD</div>
<div class="abs product-name" style="left:883px;top:970px;font-size:23px"><i></i>INVENTARIOS</div>
<div class="abs product-name" style="left:52px;top:1195px"><i></i>BANCOS</div>
<div class="abs product-name" style="left:330px;top:1192px;font-size:21px"><i></i>PRESUPUESTO</div>
<div class="abs product-name" style="left:613px;top:1192px;font-size:25px"><i></i>INVENTARIOS</div>
<div class="abs product-name" style="left:883px;top:1192px;font-size:36px"><i></i>CRM</div>

<div class="abs tile" style="left:76px;top:1043px"><i></i>VENTAS</div>
<div class="abs tile" style="left:199px;top:1043px"><i class="alt"></i>VENTAS</div>
<div class="abs tile" style="left:354px;top:1043px"><i></i>COMPRAS</div>
<div class="abs tile" style="left:476px;top:1043px"><i class="alt"></i>COMPRAS</div>
<div class="abs tile small" style="left:636px;top:1043px"><i></i>CONTABILIDAD</div>
<div class="abs tile small" style="left:759px;top:1043px"><i class="alt"></i>CONTABILIDAD</div>
<div class="abs tile small" style="left:906px;top:1043px"><i></i>INVENTARIOS</div>
<div class="abs tile small" style="left:1030px;top:1043px"><i class="alt"></i>INVENTARIOS</div>

<div class="abs tile" style="left:76px;top:1266px;font-size:16px"><i></i>BANCOS</div>
<div class="abs tile" style="left:199px;top:1266px;font-size:16px"><i class="alt"></i>BANCOS</div>
<div class="abs tile small" style="left:354px;top:1266px"><i></i>PRESUPUESTO</div>
<div class="abs tile small" style="left:476px;top:1266px"><i class="alt"></i>PRESUPUESTO</div>
<div class="abs tile small" style="left:636px;top:1266px"><i></i>INVENTARIOS</div>
<div class="abs tile small" style="left:759px;top:1266px"><i class="alt"></i>INVENTARIOS</div>
<div class="abs tile" style="left:906px;top:1266px;font-size:22px"><i></i>CRM</div>
<div class="abs tile" style="left:1030px;top:1266px;font-size:22px"><i class="alt"></i>CRM</div>

<h2 class="abs section-title profile-q" style="font-weight:400">¿Cuál es tu perfil?</h2>

<section class="abs profile blue" style="left:0">
  <h3>Profesional</h3><hr>
  <p style="top:158px">Lorem Ipsum is simply dummy text of the printing and typesetting industry has been the industry's standard text ever since the 1500s,</p>
  <p style="top:268px">when an unknown printer took a galley of type and scrambled it to make a type specimen book.</p>
  <a class="btn" style="top:364px;background:var(--blue-light)" href="#">Mas informacion</a>
</section>
<div class="abs profile" style="left:300px"><div class="ph" role="img" aria-label="Profesional independiente escribiendo en un cuaderno" style="background:linear-gradient(160deg,#d9dcdf,#f4f4f4 50%,#b9a48c)"></div></div>
<section class="abs profile light" style="left:601px">
  <h3>Contador</h3><hr>
  <p style="top:158px">Lorem Ipsum is simply dummy text of the printing and typesetting industry has been the industry's standard text ever since the 1500s,</p>
  <p style="top:268px">when an unknown printer took a galley of type and scrambled it to make a type specimen book.</p>
  <a class="btn" style="top:370px;width:154px;background:var(--blue)" href="#">Mas informacion</a>
</section>
<div class="abs profile" style="left:902px;width:298px"><div class="ph" role="img" aria-label="Contador revisando gráficos con calculadora" style="background:linear-gradient(150deg,#eef1f4,#dfe6ee 50%,#6f93bd)"></div></div>

<article class="abs plan" style="left:76px;background:var(--blue-light)">
  <h3>Micro</h3>
  <p>Lorem Ipsum is simply dummy text of the printing and typesetting industry has been the industry's standard dummy text ever since the 1500s,</p>
  <a href="#">Mas informacion</a>
</article>
<article class="abs plan" style="left:350px;background:var(--blue)">
  <h3>Micro</h3>
  <p>Lorem Ipsum is simply dummy text of the printing and typesetting industry has been the industry's standard dummy text ever since the 1500s,</p>
  <a href="#">Mas informacion</a>
</article>
<article class="abs plan" style="left:625px;background:var(--red)">
  <h3>Empresarial</h3>
  <p>Lorem Ipsum is simply dummy text of the printing and typesetting industry has been the industry's standard dummy text ever since the 1500s,</p>
  <a href="#">Mas informacion</a>
</article>
<div class="abs" role="img" aria-label="Equipo de trabajo reunido alrededor de una mesa" style="left:876px;top:2091px;width:250px;height:306px;background:linear-gradient(135deg,#8a8f93,#d9dadb 50%,#6b6f72)"></div>

<div class="abs tab tab1" style="left:197px">Tab 1</div>
<div class="abs tab tab2" style="left:404px">Tab 2</div>
<div class="abs tab tab3" style="left:606px">Tab 3</div>
<div class="abs tab tab4" style="left:811px">Tab 4</div>

<section class="abs tab-panel">
  <h2>Get Smart Chart of Accounts</h2>
  <ul class="checklist">
    <li><svg width="28" height="24" viewBox="0 0 28 24"><circle cx="12" cy="12" r="10" fill="none" stroke="#0054AA" stroke-width="2.4"/><path d="M6 12l5 5L26 3" fill="none" stroke="#0054AA" stroke-width="2.6"/></svg><span>Lorem Ipsum is simply dummy text of the printing and typesetting industry has been the industry's.</span></li>
    <li><svg width="28" height="24" viewBox="0 0 28 24"><circle cx="12" cy="12" r="10" fill="none" stroke="#0054AA" stroke-width="2.4"/><path d="M6 12l5 5L26 3" fill="none" stroke="#0054AA" stroke-width="2.6"/></svg><span>Lorem Ipsum is simply dummy text of the printing and typesetting industry has been the industry's standard dummy text ever since the 1500s,</span></li>
    <li><svg width="28" height="24" viewBox="0 0 28 24"><circle cx="12" cy="12" r="10" fill="none" stroke="#0054AA" stroke-width="2.4"/><path d="M6 12l5 5L26 3" fill="none" stroke="#0054AA" stroke-width="2.6"/></svg><span>Lorem Ipsum is simply dummy text of the printing and typesetting industry has been the industry's standard dummy text ever since the 1500s,</span></li>
    <li><svg width="28" height="24" viewBox="0 0 28 24"><circle cx="12" cy="12" r="10" fill="none" stroke="#0054AA" stroke-width="2.4"/><path d="M6 12l5 5L26 3" fill="none" stroke="#0054AA" stroke-width="2.6"/></svg><span>Lorem Ipsum is simply dummy text of the printing and typesetting industry has been the industry's.</span></li>
  </ul>
  <a class="btn" href="#">Mas informacion</a>
  <div class="tab-photo" role="img" aria-label="Persona usando una portátil con un panel de control de finanzas"></div>
</section>

<article class="abs feature" style="left:78px;background:var(--blue-light);border-radius:0 0 0 50px">
  <div class="num">1.</div><h4>Paga por uso</h4>
  <p>Lorem Ipsum is simply dummy text of the printing and typesetting.</p>
</article>
<article class="abs feature" style="left:344px;background:var(--blue);border-radius:50px 0 0 50px">
  <div class="num">2.</div><h4>Sin Contrato</h4>
  <p>Lorem Ipsum is simply dummy text of the printing and typesetting.</p>
</article>
<article class="abs feature" style="left:609px;background:var(--red);border-radius:0 0 0 50px">
  <div class="num">3.</div><h4>En La Nube</h4>
  <p>Lorem Ipsum is simply dummy text of the printing and typesetting.</p>
</article>
<article class="abs feature" style="left:875px;background:var(--black);border-radius:0 0 0 50px">
  <div class="num">4.</div><h4 style="font-size:20px">Multiples Dispositivos</h4>
  <p>Lorem Ipsum is simply dummy text of the printing and typesetting.</p>
</article>

<section class="abs cta">
  <h2>?Que Esperas Para Crear Una Cuenta Gratis En Cuentix?</h2>
  <a class="btn" href="#">Crear Cuenta Gratis</a>
</section>
<div class="abs cta-photo" role="img" aria-label="Mano con bolígrafo sobre una calculadora y gráficos financieros"></div>

<footer class="abs site-footer">
  <div class="brand"><span class="brand-dot"></span>Cuentix</div>
  <div class="newsletter-input">Reciba Las actualizaciones de Cuentix</div>
  <a class="newsletter-btn" href="#">Suscribirme</a>
</footer>

</body>
</html>
```